Home page makeover

Take my existing home page, www.maplecrestharborline.com and redesign layout to look more current considering today's touch design prevalence.
Reuse existing elements or suggest improved ones if available.
I generally have average CSS and HTML skills using div containers, defining lists and using columns to create the code to support the layout.
Updates
Just wanted to send out a quick message to thank all of you for your submissions. Many of you offered nice designs, but unfortunately could only choose one.
Target Market(s)
Generally targeting individuals with some assets for retirement. Basically your average working professional or business owner.
Industry/Entity Type
It Support
Look and feel
Each slider illustrates characteristics of the customer's brand and the style your logo design should communicate.

```html
<!DOCTYPE html>
<html lang="en">
<head>
<meta charset="utf-8">
<title>Maplecrest Harborline – Home</title>
<link rel="stylesheet" href="https://fonts.googleapis.com/css2?family=Amaranth:wght@400;700&family=Oswald:wght@400;500;700&family=Arvo:wght@400;700&family=Open+Sans:wght@400;600&family=Roboto:wght@400;700;900&display=swap">
<style>
:root{
  --green-dark:#0b5a1f;
  --green-mid:#2f8b45;
  --green-soft:#8cc97a;
  --green-lime:#8dc63f;
  --green-bright:#7ed957;
  --text:#5a5a5a;
  --box:#e3e3e3;
  --white:#ffffff;
}
*{margin:0;padding:0;box-sizing:border-box}
html,body{width:825px;height:1200px;overflow:hidden;background:var(--white)}
body{position:relative;font-family:"Open Sans",sans-serif;color:var(--text)}
.abs{position:absolute}

.site-header{left:0;top:0;width:825px;height:61px;background:var(--green-dark)}
.brand{left:92px;top:13px;display:flex;align-items:center;gap:8px;color:var(--white)}
.brand-mark{width:34px;height:34px;background:var(--green-lime)}
.brand-name{font-family:"Amaranth",sans-serif;font-size:34px;line-height:34px;font-weight:700}
.nav a{position:absolute;top:0;height:61px;line-height:61px;font-family:"Oswald",sans-serif;font-size:12px;color:var(--white);text-decoration:none;text-align:center}
.nav .active{background:var(--green-mid)}
.btn{position:absolute;font-family:"Oswald",sans-serif;font-size:12px;color:var(--white);text-align:center;border-radius:2px}
.btn-signin{left:604px;top:19px;width:62px;height:23px;line-height:23px;background:var(--green-lime)}
.btn-signup{left:672px;top:19px;width:62px;height:23px;line-height:23px;background:var(--green-mid)}

.hero{left:0;top:61px;width:825px;height:280px;background:radial-gradient(ellipse at 50% 40%,#d9f2c8 0%,#a6e46e 45%,#7fd23c 100%)}
.slider{left:90px;top:62px;width:645px;height:258px;background:linear-gradient(90deg,#dfe9e3,#edf3ef);box-shadow:0 2px 3px rgba(0,0,0,.35);overflow:hidden}
.slide-photo{left:0;top:0;width:400px;height:258px;background:linear-gradient(180deg,#bcd6ea 0%,#e6eef2 45%,#c9b89b 75%,#8a6f55 100%)}
.slide-fade{left:300px;top:0;width:120px;height:258px;background:linear-gradient(90deg,rgba(228,238,232,0),#e4eee8)}
.slide-title{left:389px;top:34px;font-family:"Oswald",sans-serif;font-weight:700;font-size:52px;line-height:62px;color:var(--green-dark);letter-spacing:1px}
.slide-text{left:389px;top:102px;width:228px;font-family:"Arvo",serif;font-size:9.4px;line-height:15.4px;color:#555}
.btn-slide{left:389px;top:176px;width:74px;height:25px;line-height:25px;background:var(--green-soft)}
.dots{left:533px;top:234px;display:flex;gap:3px}
.dots span{width:29px;height:3px;background:#b8e0a8}
.dots span:first-child{background:var(--green-dark)}

.welcome-title{left:0;top:355px;width:825px;text-align:center;font-family:"Amaranth",sans-serif;font-weight:400;font-size:21px;color:var(--green-dark)}
.welcome-text{left:105px;top:390px;width:615px;text-align:center;font-size:9.6px;line-height:15.4px}
.btn-more{left:375px;top:448px;width:75px;height:25px;line-height:25px;background:var(--green-soft)}

.pricing{left:90px;top:499px;width:645px;height:52px;border-radius:3px;background:linear-gradient(180deg,#3a3a3a,#0e0e0e);box-shadow:0 2px 3px rgba(0,0,0,.3);overflow:hidden}
.pricing-cta{left:0;top:0;width:645px;height:52px}
.pricing-cta-label{left:31px;top:10px;font-family:"Roboto",sans-serif;font-weight:900;font-size:26px;color:var(--white)}
.price{font-family:"Roboto",sans-serif;color:var(--white)}
.price b{font-size:25px;font-weight:700;line-height:28px}
.price b em{font-style:normal;color:var(--green-bright)}
.price small{display:block;font-size:11px;color:var(--green-bright);line-height:12px}
.pricing-divider{left:418px;top:0;width:1px;height:52px;background:#444}

.section-title{font-family:"Amaranth",sans-serif;font-weight:400;font-size:20px;color:var(--green-dark)}
.features{left:90px;top:609px;width:309px;list-style:none}
.features li{background:var(--box);border-radius:3px;padding:7px 9px;margin-bottom:3px;font-size:9.4px;line-height:13.6px}
.video{left:425px;top:608px;width:309px;height:214px;background:#000}
.video-title{left:6px;top:4px;font-size:8px;color:var(--white)}
.video-frame{left:38px;top:18px;width:233px;height:168px;background:linear-gradient(135deg,#e6e6e6,#8c8c8c 60%,#bdbdbd)}
.video-word{left:46px;top:118px;font-family:"Roboto",sans-serif;font-weight:900;font-style:italic;font-size:28px;color:var(--white)}
.video-play{left:131px;top:81px;width:45px;height:32px;border-radius:7px;background:#1b1b1b}
.video-bar{left:0;top:192px;width:309px;height:22px;background:#1a1a1a}
.video-progress{left:4px;top:195px;width:301px;height:2px;background:#555}
.video-time{left:60px;top:202px;font-size:7px;color:#ccc}

.testi-rule{left:90px;top:920px;width:645px;height:2px;background:var(--green-dark)}
.testi-badge{left:322px;top:908px}
.testi-label{left:322px;top:910px;width:180px;text-align:center;font-family:"Amaranth",sans-serif;font-weight:400;font-size:19px;color:var(--white)}
.testimonial{width:300px;height:60px}
.avatar{left:0;top:0;width:53px;height:53px;border-radius:50%;background:radial-gradient(circle,#e2c2aa,#8a5a42);border:2px solid #e9e9e9}
.quote{left:73px;top:2px;width:225px;font-size:9.4px;line-height:13.6px}
.author{font-size:9.4px;color:var(--green-dark);margin-top:10px}
.testi-sep{height:1px;background:#e2e2e2}

.site-footer{left:0;top:1132px;width:825px;height:68px;background:var(--green-dark)}
.footer-title{left:90px;top:1141px;font-family:"Amaranth",sans-serif;font-weight:400;font-size:15px;color:var(--white)}
.newsletter-input{left:90px;top:1165px;width:167px;height:21px;background:var(--white);font-size:9.5px;line-height:21px;padding-left:7px;color:#444}
.newsletter-submit{left:257px;top:1165px;width:46px;height:21px;line-height:21px;background:var(--green-mid);font-family:"Open Sans",sans-serif;font-size:9px}
.social{width:25px;height:25px;border-radius:50%;background:#3f9a3c;top:1146px}
.copyright{left:480px;top:1176px;width:255px;text-align:right;font-size:8.5px;color:var(--white)}
</style>
</head>
<body>

<header class="abs site-header">
  <div class="abs brand"><span class="brand-mark"></span><span class="brand-name">MHL</span></div>
  <nav class="nav">
    <a class="active" style="left:400px;width:50px">HOME</a>
    <a style="left:460px;width:46px">ABOUT</a>
    <a style="left:521px;width:55px">CONTACT</a>
  </nav>
  <span class="btn btn-signin">SIGN IN</span>
  <span class="btn btn-signup">SIGN UP</span>
</header>

<section class="abs hero"></section>
<div class="abs slider">
  <div class="abs slide-photo" role="img" aria-label="Photo of a rope hammock on a seaside porch"></div>
  <div class="abs slide-fade"></div>
  <h1 class="abs slide-title">RETIRE</h1>
  <p class="abs slide-text">Identify and project your retirement needs and expectations including basic living expenses, housing costs, recreation, big ticket non-recurring items, medical and nursing home care</p>
  <span class="btn btn-slide">SHOW MORE</span>
  <div class="abs dots"><span></span><span></span><span></span></div>
</div>

<h2 class="abs welcome-title">Welcome To Maplecrest Harborline</h2>
<p class="abs welcome-text">Our mission is to help you make the basic determination of when and how you can retire. This site will provide the average individual a comprehensive tool to assist with managing this daunting proposition and help you identify a realistic age that you can retire given your expectations and needs during retirement considering all of your available resources.</p>
<span class="btn btn-more">SHOW MORE</span>

<div class="abs pricing">
  <svg class="abs pricing-cta" width="645" height="52" viewBox="0 0 645 52" aria-hidden="true">
    <defs><linearGradient id="ctaGreen" x1="0" y1="0" x2="0" y2="1"><stop offset="0" stop-color="#3fae3a"/><stop offset="1" stop-color="#0f6a1c"/></linearGradient></defs>
    <path d="M0 0H165Q175 0 180 20L190 52H0Z" fill="url(#ctaGreen)"/>
  </svg>
  <span class="abs pricing-cta-label">SIGN UP</span>
  <div class="abs price" style="left:232px;top:5px"><b><em>Only</em> $19.99</b><small>For a One Year Membership</small></div>
  <div class="abs pricing-divider"></div>
  <div class="abs price" style="left:462px;top:5px"><b><em>Only</em> $9.99</b><small>Per Year After That</small></div>
</div>

<h2 class="abs section-title" style="left:90px;top:573px">Features</h2>
<ul class="abs features">
  <li>Identify and project your retirement needs and expectations including basic living expenses, housing costs, recreation, big ticket non-recurring items, medical and nursing home care.</li>
  <li>Identify and project all your sources of retirement income including retirement savings, other savings, pension plans, Social Security, life insurance and working part-time during retirement for a period of time.</li>
  <li>Strategize tapping into the equity of your real estate including swapping your primary residence for a different home or retirement area, or selling and renting.</li>
  <li>Produce easy to understand results featuring the Retirement Readiness Gauge™.</li>
  <li>Save your work so you can return, revisit and edit your retirement plan at a later date.</li>
</ul>

<h2 class="abs section-title" style="left:425px;top:573px">Our Video</h2>
<div class="abs video">
  <span class="abs video-title">Demo.wmv</span>
  <div class="abs video-frame" role="img" aria-label="Video still of a laptop keyboard with reading glasses"></div>
  <span class="abs video-word">Plan</span>
  <div class="abs video-play"></div>
  <svg class="abs" style="left:147px;top:90px" width="14" height="14" viewBox="0 0 14 14" aria-hidden="true"><path d="M2 1L13 7L2 13Z" fill="#fff"/></svg>
  <div class="abs video-bar"></div>
  <div class="abs video-progress"></div>
  <svg class="abs" style="left:12px;top:201px" width="40" height="10" viewBox="0 0 40 10" aria-hidden="true"><path d="M0 1L7 5L0 9Z" fill="#aaa"/><path d="M24 3H27L31 0V10L27 7H24Z" fill="#aaa"/></svg>
  <span class="abs video-time">0:00 / 0:28</span>
</div>

<div class="abs testi-rule"></div>
<svg class="abs testi-badge" width="180" height="30" viewBox="0 0 180 30" aria-hidden="true">
  <path d="M12 0H168L180 15L168 30H12L0 15Z" fill="#0b5a1f"/>
  <circle cx="17" cy="15" r="3.5" fill="#fff"/><circle cx="163" cy="15" r="3.5" fill="#fff"/>
</svg>
<h2 class="abs testi-label">Testimonials</h2>

<div class="abs testimonial" style="left:90px;top:961px">
  <div class="abs avatar" role="img" aria-label="Portrait of a client"></div>
  <div class="abs quote">“I can see professionals using this site to validate their existing retirement plans”<p class="author">- Owen, New Jersey</p></div>
</div>
<div class="abs testimonial" style="left:425px;top:961px">
  <div class="abs avatar" role="img" aria-label="Portrait of a client"></div>
  <div class="abs quote">“This site is a great place to get a handle on your retirement strategy”<p class="author">- Dana, New Jersey</p></div>
</div>
<div class="abs testi-sep" style="left:90px;top:1030px;width:310px"></div>
<div class="abs testi-sep" style="left:425px;top:1030px;width:310px"></div>
<div class="abs" style="left:412px;top:960px;width:1px;height:142px;background:#e2e2e2"></div>
<div class="abs testimonial" style="left:90px;top:1047px">
  <div class="abs avatar" role="img" aria-label="Portrait of a client"></div>
  <div class="abs quote">“It's the only retirement projection tool for the average user that puts it all together”<p class="author">- Glen, New York</p></div>
</div>
<div class="abs testimonial" style="left:425px;top:1047px">
  <div class="abs avatar" role="img" aria-label="Portrait of a client"></div>
  <div class="abs quote">“Many people really need to do this”<p class="author">- Rita, New York</p></div>
</div>

<footer class="abs site-footer"></footer>
<h3 class="abs footer-title">Newsletter Updates</h3>
<div class="abs newsletter-input">Enter Email here...</div>
<span class="btn newsletter-submit">SUBMIT</span>
<span class="abs social" style="left:678px"></span>
<span class="abs social" style="left:709px"></span>
<p class="abs copyright">© 2013 Maplecrest Harborline. All Rights Reserved.</p>

</body>
</html>
```